Business card and stationary design for construction company
RT Garland Construction
Business card and stationary design for construction company - Construction
Creative Brief
Professional
Marcus Garland
President
781 Willow Bend Dr Santa Rosa Beach, FL 32617
marcus@rt-garland.example
rt-garland.example

```html
<!DOCTYPE html>
<html lang="en">
<head>
<meta charset="utf-8">
<title>RT Garland Construction — Business Cards</title>
<link rel="stylesheet" href="https://fonts.googleapis.com/css2?family=Roboto:wght@400;500;700&family=Roboto+Condensed:wght@700&display=swap">
<style>
  :root {
    --navy: #1c2d68;
    --navy-deep: #142253;
    --royal: #2b4fa3;
    --sky: #3f74c9;
    --white: #ffffff;
    --ink: #1f2a44;
    --stage: #e9ebef;
  }
  * { box-sizing: border-box; margin: 0; padding: 0; }
  html, body {
    width: 1200px; height: 908px; overflow: hidden;
    background: var(--stage);
    font-family: "Roboto", Arial, sans-serif;
  }
  .sheet {
    position: relative; width: 1200px; height: 908px;
    display: flex; flex-direction: column; align-items: center; justify-content: center; gap: 46px;
  }
  .card {
    position: relative; width: 660px; height: 377px;
    border-radius: 22px; overflow: hidden;
    box-shadow: 0 8px 22px rgba(20, 34, 83, 0.18);
  }

  /* Front */
  .card-front {
    background: linear-gradient(135deg, var(--navy-deep) 0%, var(--navy) 55%, var(--royal) 100%);
    color: var(--white);
  }
  .brand {
    position: absolute; display: flex; align-items: center; gap: 12px;
    font-family: "Roboto Condensed", Arial, sans-serif; font-weight: 700;
    text-transform: uppercase; letter-spacing: 1px; line-height: 1.05;
  }
  .brand-mark { width: 18px; height: 18px; flex: none; }
  .card-front .brand { left: 48px; top: 96px; font-size: 30px; color: var(--white); }
  .card-front .brand-mark { background: var(--white); }
  .services {
    position: absolute; left: 52px; bottom: 58px; list-style: none;
    font-size: 24px; line-height: 1.35; font-weight: 400;
  }
  .services li::before {
    content: ""; display: inline-block; width: 8px; height: 8px; border-radius: 50%;
    background: var(--white); margin-right: 12px; vertical-align: middle;
  }

  /* Back */
  .card-back { background: var(--white); color: var(--ink); }
  .card-back svg.waves { position: absolute; inset: 0; width: 100%; height: 100%; }
  .card-back .brand { right: 48px; top: 120px; font-size: 26px; color: var(--navy); }
  .card-back .brand-mark { background: var(--navy); }
  .person { position: absolute; right: 48px; top: 190px; text-align: right; }
  .person-name { font-size: 24px; font-weight: 700; color: var(--navy); }
  .person-title { font-size: 18px; font-weight: 500; color: var(--sky); margin-top: 2px; }
  .contact {
    position: absolute; left: 44px; bottom: 38px; font-size: 15px; line-height: 1.45;
    color: var(--ink); font-style: normal;
  }
  .contact-row { display: flex; align-items: center; gap: 8px; }
  .contact-icon { width: 16px; height: 16px; flex: none; }
</style>
</head>
<body>
<main class="sheet">

  <section class="card card-front" aria-label="Business card front">
    <div class="brand"><span class="brand-mark"></span><span>RT Garland<br>Construction</span></div>
    <ul class="services">
      <li>Commercial</li>
      <li>Industrial</li>
      <li>Residential</li>
    </ul>
  </section>

  <section class="card card-back" aria-label="Business card back">
    <svg class="waves" viewBox="0 0 660 377" preserveAspectRatio="none" aria-hidden="true">
      <path d="M0 0 H660 V40 C520 30 360 40 200 80 C120 100 50 110 0 108 Z" fill="var(--navy)"/>
      <path d="M0 108 C50 110 120 100 200 80 C360 40 520 30 660 40 V52 C520 44 370 54 210 92 C130 112 60 122 0 122 Z" fill="var(--sky)"/>
      <path d="M0 362 C200 352 420 350 660 320 V377 H0 Z" fill="var(--navy)"/>
      <path d="M0 356 C200 346 420 342 660 310 V320 C420 350 200 352 0 362 Z" fill="var(--sky)"/>
    </svg>

    <div class="brand"><span class="brand-mark"></span><span>RT Garland<br>Construction</span></div>

    <div class="person">
      <div class="person-name">Marcus Garland</div>
      <div class="person-title">President</div>
    </div>

    <address class="contact">
      <div>781 Willow Bend Dr</div>
      <div>Cedar Hollow, FL 32617</div>
      <div class="contact-row">
        <svg class="contact-icon" viewBox="0 0 16 16" aria-hidden="true"><circle cx="8" cy="8" r="8" fill="var(--navy)"/><path d="M5.3 4.2 6.6 4l.8 2-1 .7a5 5 0 0 0 2.4 2.4l.7-1 2 .8-.2 1.3c-3.4.4-6.3-2.5-6-6Z" fill="#fff"/></svg>
        <span>555-010-2236</span>
      </div>
      <div class="contact-row">
        <svg class="contact-icon" viewBox="0 0 16 16" aria-hidden="true"><circle cx="8" cy="8" r="8" fill="var(--navy)"/><rect x="4" y="5.2" width="8" height="5.6" rx="0.8" fill="#fff"/><path d="M4.3 5.6 8 8.4l3.7-2.8" stroke="var(--navy)" stroke-width="0.9" fill="none"/></svg>
        <span>marcus@rt-garland.example</span>
      </div>
      <div class="contact-row">
        <svg class="contact-icon" viewBox="0 0 16 16" aria-hidden="true"><circle cx="8" cy="8" r="8" fill="var(--navy)"/><circle cx="8" cy="8" r="4" fill="none" stroke="#fff" stroke-width="1"/><path d="M4 8h8M8 4c-1.6 2.2-1.6 5.8 0 8M8 4c1.6 2.2 1.6 5.8 0 8" stroke="#fff" stroke-width="0.8" fill="none"/></svg>
        <span>rt-garland.example</span>
      </div>
    </address>
  </section>

</main>
</body>
</html>
```